Author needs a book cover design for a science fiction novel

My name is Pavel Drummond. I need a book cover design for my science fiction novel - "Rusty Pepper Moon"
In the 36th century a giant comet is hurtling through space on a collision course with Earth. On its way past Pluto the people of Pluto decide to offer a message of encouragement. They place a huge sign on the comet - RUSTY PEPPER MOON in huge red neon letters. (The words RUSTY PEPPER are on top of the word MOON). So the first thing I need on my cover is the comet with the Rusty Pepper Moon sign.
A woman from a time well beyond the 36th century then makes an appearance. She has put the comet on a collision course with Earth in order to protect her own timeline. Her character is an ode to the Sirens of Greek mythology who use their great beauty to lure sailors to their death. She has red hair with a hint of metallic blue, hypnotic blue eyes with a swirl of green, effervescent red lips, a tattoo on her left cheekbone of six blue doves flying in a circle, a short golden dress that shows plenty of cleavage, an Egyption style large golden collar necklace, sandals with leather straps that wind up her calves, fingernails that pulse through the colours of the rainbow in arcs of colour that jump from fingernail to fingernail. So the second thing I need on the cover is a representation of this woman. Prehaps just her face with a wicked smile looking over the comet, but I am open to any variation of the comet and the woman. Done well I think it would make for a very striking book cover.

I would also like PAVEL DRUMMOND written along the bottom of the cover, along with PAVEL DRUMMOND and RUSTY PEPPER MOON on the side.

On the Back cover the following blurb:

The unlikely hero:
In 1984 sixteen year old Barlow follows the advice of a mysterious stranger and sneaks a note into a time capsule that is to be buried at his school. The note is a request to be taken to the future once time travel has been developed. Years later, just when his mundane life is about to come to a sudden and premature end, the prophesy of the note is fulfilled and he finds himself rescued and catapulted into a future world beyond his imagination. He is a man out of his time and out of his depth, but even so he finds that the fate of the human race rests in his hands.

The rescuer:
Toby is a time traveller from the 36th century tasked to rescue Barlow. To Toby’s horror when he arrives back in the 36th century with Barlow he finds the timeline in ruins and his world populated by a strange alternative civilisation. Toby and Barlow zip about through time in an attempt to unravel the mystery only to find the more they dabble with time the worse things become.

The Siren:
She’s wickedly beautiful, dangerous to mess with and from an unknown time eons into the future. She puts a giant comet on a collision course with 36th century Earth. Just what she is up to is a mystery that seems impossible to solve, anyone who looks into her hypnotic blue eyes instantly turns into a love struck idiot. Barlow thinks that he is strong enough to take her on, but is she really such a big player in the game? Or just a diversionary tactic controlled by a higher power?

Brief updated with better guidelines for what is required.

Clarification on the sign: The sign is flat and sticks to the comet like a stamp. The people of pluto built the sign in space in the path of the comet, the comet ran into it, the sign stuck to the comet. The comet is round and 11 km in diameter. The sign takes up most of the face of the comet, with RUSTY PEPPER written on top of MOON. The sign is tranparent apart from the letters, which are neon red.

Reason: Designers have requested more time.

Does anyone need more time?

Reason: More time needed to finish designs

Target Market(s)

Science fiction fans, the story is not hardcore sci-fi. It is a light hearted romp through time with plenty of humour. I am aiming to release as an eBook and possibly a paper version as well. Size of front cover 6" x 9"

Industry/Entity Type

Tattoo

Colors

Designer to choose colors to be used in the design.

Requirements
Must have
• Comet on the front cover with RUSTYS PEPPER MOON sign written on it in large neon letters. The words RUSTY PEPPER on top and MOON below. The sign takes up most of the space on the face of the comet.
The woman as described earlier, must be very attractive with a wicked smile. Either her face above the comet, or whole body, perhaps beckoning the comet towards the Earth with her rainbow fingers. Or some other combination of the comet and woman that looks good. I would like her to look sexy, imposing and classy, not cheesy or sleazy.
Nice to have
• Prefer that the woman have red hair with a hint of metallic blue, but if you think another colour looks better go with it and I can change her hair colour in the book to match. Change her golden dress too if another outfit looks better.
Should not have
• Rusty Pepper Moon in small writing, woman who doesn't look stunning. Gold collar necklace shouldn't be so big as to be a distraction.
I want people to look at the cover and think, wow this looks interesting, and who is she?

```html
<!DOCTYPE html>
<html lang="en">
<head>
<meta charset="UTF-8">
<title>Rusty Pepper Moon — Book Cover Spread</title>
<link href="https://fonts.googleapis.com/css2?family=Oswald:wght@300;400;500;700&display=swap" rel="stylesheet">
<style>
  :root {
    --page-bg: #ececec;
    --cover-black: #0b0b0b;
    --title-grey: #d9d9d9;
    --body-grey: #e4e4e4;
    --box-dark: #151515;
    --box-label: #5a5a5a;
    --sky-gold: #e7b23a;
    --sky-haze: #c9b98a;
    --sky-blue: #3f6fb4;
    --deep-blue: #0f2f78;
    --night-blue: #081a4a;
    --neon-line: #eaf3ff;
    --neon-glow: #2f7bff;
    --white: #ffffff;
  }
  * { box-sizing: border-box; margin: 0; padding: 0; }
  html, body {
    width: 1200px; height: 800px; overflow: hidden;
    background: var(--page-bg);
    font-family: "Oswald", "Arial Narrow", sans-serif;
  }
  .spread {
    position: absolute; left: 140px; top: 70px;
    width: 920px; height: 660px;
    display: flex;
    box-shadow: 0 18px 40px rgba(0,0,0,0.18);
  }

  /* Back cover */
  .back-cover {
    width: 440px; height: 660px;
    background: var(--cover-black);
    color: var(--body-grey);
    padding: 30px 40px 0;
    position: relative;
  }
  .back-author {
    text-align: right; font-weight: 500; font-size: 13px;
    letter-spacing: 0.5px; color: var(--title-grey);
  }
  .back-title {
    font-weight: 700; font-size: 42px; line-height: 1;
    color: var(--title-grey); text-align: right;
    letter-spacing: 0.5px; margin-top: 2px; white-space: nowrap;
  }
  .blurb { margin-top: 20px; }
  .blurb-heading {
    text-align: center; font-weight: 500; font-size: 12px;
    text-transform: uppercase; margin: 14px 0 3px;
    color: var(--white);
  }
  .blurb-heading:first-child { margin-top: 0; }
  .blurb p {
    font-weight: 400; font-size: 12px; line-height: 1.4;
    text-align: justify; text-align-last: center;
    color: var(--body-grey);
  }
  .isbn-box {
    position: absolute; left: 72px; bottom: 36px;
    width: 86px; height: 64px; background: var(--box-dark);
    color: var(--box-label); font-size: 7px; text-align: center;
    padding-top: 24px; letter-spacing: 0.5px;
  }

  /* Spine */
  .spine {
    width: 40px; height: 660px;
    background: var(--cover-black);
    position: relative;
  }
  .spine-title {
    position: absolute; left: 50%; top: 18px;
    writing-mode: vertical-rl;
    transform: translateX(-50%);
    font-weight: 500; font-size: 22px; letter-spacing: 6px;
    color: var(--title-grey); white-space: nowrap;
  }
  .spine-author {
    position: absolute; left: 50%; bottom: 30px;
    writing-mode: vertical-rl;
    transform: translateX(-50%);
    font-weight: 400; font-size: 8px; letter-spacing: 1.5px;
    color: var(--title-grey); white-space: nowrap;
  }

  /* Front cover */
  .front-cover {
    width: 440px; height: 660px; position: relative; overflow: hidden;
  }
  .cover-art {
    position: absolute; inset: 0;
    background:
      radial-gradient(ellipse 40% 18% at 50% 92%, #6f95d0 0%, var(--deep-blue) 70%, transparent 100%),
      linear-gradient(180deg, var(--sky-gold) 0%, var(--sky-haze) 30%, var(--sky-blue) 55%, var(--deep-blue) 78%, var(--night-blue) 100%);
  }
  .front-title {
    position: absolute; left: 0; top: 0;
    width: 440px; height: 420px;
  }
  .front-title text {
    font-family: "Oswald", "Arial Narrow", sans-serif;
    font-weight: 700; font-size: 112px; letter-spacing: 2px;
    fill: none; stroke: var(--neon-line); stroke-width: 3.5;
  }
  .front-author {
    position: absolute; left: 0; right: 0; bottom: 30px;
    text-align: center; color: var(--white);
    font-weight: 700; font-size: 22px; letter-spacing: 1px;
  }
</style>
</head>
<body>
  <main class="spread">
    <section class="back-cover">
      <div class="back-author">PAVEL DRUMMOND</div>
      <h2 class="back-title">RUSTY PEPPER MOON</h2>
      <div class="blurb">
        <h3 class="blurb-heading">The unlikely hero:</h3>
        <p>In 1984 sixteen year old Barlow follows the advice of a mysterious stranger and sneaks a note into a time capsule that is to be buried at his school. The note is a request to be taken to the future once time travel has been developed. Years later, just when his mundane life is about to come to a sudden and premature end, the prophesy of the note is fulfilled and he finds himself rescued and catapulted into a future world beyond his imagination. He is a man out of his time and out of his depth, but even so he finds that the fate of the human race rests in his hands.</p>
        <h3 class="blurb-heading">The rescuer:</h3>
        <p>Toby is a time traveller from the 36th century tasked to rescue Barlow. To Toby’s horror when he arrives back in the 36th century with Barlow he finds the timeline in ruins and his world populated by a strange alternative civilisation. Toby and Barlow zip about through time in an attempt to unravel the mystery only to find the more they dabble with time the worse things become.</p>
        <h3 class="blurb-heading">The siren:</h3>
        <p>She’s wickedly beautiful, dangerous to mess with and from an unknown time eons into the future. She puts a giant comet on a collision course with 36th century Earth. Just what she is up to is a mystery that seems impossible to solve, anyone who looks into her hypnotic blue eyes instantly turns into a love struck idiot. Barlow thinks that he is strong enough to take her on, but is she really such a big player in the game? Or just a diversionary tactic controlled by a higher power?</p>
      </div>
      <div class="isbn-box">ISBN</div>
    </section>

    <section class="spine">
      <div class="spine-title">RUSTY PEPPER MOON</div>
      <div class="spine-author">PAVEL DRUMMOND</div>
    </section>

    <section class="front-cover">
      <div class="cover-art" role="img" aria-label="Cosmic sky glowing gold above and deep blue below, with a lightning bolt striking down onto the globe of a planet among blue clouds"></div>
      <svg class="front-title" viewBox="0 0 440 420" aria-labelledby="front-title-text">
        <title id="front-title-text">RUSTY PEPPER MOON</title>
        <defs>
          <filter id="neon-glow" x="-20%" y="-20%" width="140%" height="140%">
            <feMorphology in="SourceAlpha" operator="dilate" radius="2" result="thick"/>
            <feGaussianBlur in="thick" stdDeviation="5" result="blur"/>
            <feFlood flood-color="#2f7bff"/>
            <feComposite operator="in" in2="blur" result="glow"/>
            <feMerge>
              <feMergeNode in="glow"/>
              <feMergeNode in="glow"/>
              <feMergeNode in="SourceGraphic"/>
            </feMerge>
          </filter>
        </defs>
        <g filter="url(#neon-glow)" text-anchor="middle">
          <text x="220" y="150">RUSTY</text>
          <text x="220" y="262">PEPPER</text>
          <text x="220" y="374">MOON</text>
        </g>
      </svg>
      <div class="front-author">PAVEL DRUMMOND</div>
    </section>
  </main>
</body>
</html>
```